Intermodal Trucking Company Website

My client is a trucking company that takes the containers you see on the back of a ship or railroad car and delivers them in the midwestern part of the United States. Here are some of their competitors Websites and their logo to use as part of the design.

http://www.varnekhaulers.example/
https://www.plirext.example/
http://www.brontagefreight.example/
https://www.lqp-xy.example/

Industry/Entity Type

Trucking Company

Number of Pages Required

2 page

Requirements
Must have
• Website must be professional and the design needs to be suitable for a responsive Website.
Should not have
• Please do not submit designs with misspellings. Designs with misspellings will be eliminated.

```html
<!DOCTYPE html>
<html lang="en">
<head>
<meta charset="utf-8">
<title>Dorrance Haul Co — Intermodal Trucking</title>
<link rel="stylesheet" href="https://fonts.googleapis.com/css2?family=Carlito:ital,wght@0,400;0,700;1,400&family=Arimo:wght@400&display=swap">
<style>
  :root {
    --orange: #d64d27;
    --yellow: #f0cf2e;
    --hero-yellow: #f6e532;
    --white: #ffffff;
    --ink: #1a1a1a;
    --muted: #a9a9b3;
    --contact-bg: #ededf5;
    --footer-bg: #000000;
    --footer-text: #9a9a9a;
  }
  * { box-sizing: border-box; margin: 0; padding: 0; }
  html, body { width: 667px; height: 1200px; overflow: hidden; background: var(--white); }
  body { position: relative; font-family: "Carlito", Calibri, sans-serif; color: var(--ink); }
  .abs { position: absolute; }

  /* Hero */
  .hero { left: 0; top: 0; width: 667px; height: 430px; overflow: hidden;
    background: linear-gradient(180deg, #2c3446 0%, #5b5460 22%, #b86a3c 36%, #3a3130 52%, #1f1c1d 75%, #121213 100%); }
  .hero-photo { left: 82px; top: 155px; width: 494px; height: 160px;
    background: linear-gradient(90deg, #c9a92a 0%, #e2c53a 55%, #d9d9d9 70%, #9a9a9a 100%); opacity: .5; }
  .brand { left: 100px; top: 16px; width: 110px; text-align: center; color: var(--hero-yellow); font-size: 12px; font-weight: 700; line-height: 1.15; white-space: nowrap; }
  .brand .mark { display: block; width: 24px; height: 24px; border-radius: 50%; background: var(--orange); margin: 0 auto 5px; }
  .brand small { display: block; font-size: 9px; }
  .nav { top: 45px; left: 343px; font-size: 8px; color: var(--white); }
  .nav a { color: inherit; text-decoration: none; position: absolute; white-space: nowrap; }
  .nav a.active { color: var(--hero-yellow); }
  .social { display: flex; gap: 4px; }
  .social span { width: 16px; height: 16px; border-radius: 50%; border: 1.5px solid currentColor; display: block; }
  .hero-social { left: 483px; top: 17px; color: #5a5a5a; }
  .hero-title { left: 108px; top: 222px; font-size: 33px; color: var(--hero-yellow); font-weight: 400; white-space: nowrap; }
  .hero-text { left: 110px; top: 261px; width: 260px; font-size: 8.5px; font-style: italic; line-height: 1.3; color: var(--white); }
  .btn-outline { left: 109px; top: 318px; width: 104px; height: 28px; border: 1px solid var(--hero-yellow); padding: 2px; }
  .btn-outline span { display: flex; align-items: center; justify-content: center; width: 100%; height: 100%; border: 1px solid var(--hero-yellow); color: var(--white); font-size: 10px; }
  .dots { left: 322px; top: 421px; display: flex; gap: 1px; }
  .dots i { width: 7px; height: 7px; border-radius: 50%; border: 1px solid var(--white); display: block; }
  .dots i.on { background: var(--hero-yellow); border-color: var(--hero-yellow); }

  /* About */
  .about-title { left: 0; width: 667px; top: 440px; text-align: center; color: var(--orange); font-size: 16px; font-weight: 400; }
  .about-text { left: 118px; width: 431px; top: 466px; text-align: center; color: var(--muted); font-size: 7.5px; font-style: italic; line-height: 1.4; }

  /* Split */
  .split-left { left: 0; top: 528px; width: 343px; height: 246px; background: var(--orange); }
  .split-right { left: 343px; top: 528px; width: 324px; height: 246px; background: var(--yellow); }
  .dash { left: 0; width: 667px; border-top: 1px dashed rgba(255,255,255,.6); }
  .split-heading { font-size: 14.5px; font-weight: 400; }
  .who-title { left: 110px; top: 557px; color: var(--hero-yellow); }
  .what-title { left: 355px; top: 557px; color: var(--orange); }
  .split-text { width: 215px; font-size: 6.8px; font-style: italic; line-height: 1.45; color: var(--white); }
  .who-text { left: 110px; top: 585px; }
  .what-text { left: 355px; top: 583px; }
  .learn-more { font-size: 6.8px; font-style: italic; }
  .who-more { left: 111px; top: 712px; color: var(--hero-yellow); }
  .what-more { left: 521px; top: 712px; color: var(--orange); }
  .split-brand { left: 296px; top: 728px; display: flex; align-items: center; gap: 5px; color: var(--ink); font-size: 11px; font-weight: 700; white-space: nowrap; }
  .split-brand i { width: 14px; height: 14px; border-radius: 50%; background: var(--orange); border: 1px solid var(--white); display: block; flex: none; }

  /* Feature band */
  .band { left: 0; top: 774px; width: 667px; height: 160px;
    background: linear-gradient(90deg, #3a3430 0%, #5a4b42 30%, #5e1f1c 55%, #3b2a25 75%, #6e6a66 100%); }
  .band-title { left: 110px; top: 787px; color: var(--white); font-size: 15.5px; line-height: 1.35; font-weight: 400; }
  .band-text { left: 110px; top: 853px; width: 210px; font-size: 6.8px; font-style: italic; line-height: 1.4; color: var(--white); }
  .band-more { left: 111px; top: 895px; color: var(--hero-yellow); }

  /* Contact */
  .contact { left: 0; top: 934px; width: 667px; height: 211px; background: var(--contact-bg); }
  .contact-title { left: 110px; top: 959px; color: var(--orange); font-size: 23px; font-weight: 400; }
  .field { left: 108px; width: 128px; border-bottom: 1px solid #dcdce4; font-size: 7.5px; color: var(--muted); padding-bottom: 6px; }
  .submit { left: 110px; top: 1093px; width: 101px; height: 25px; background: var(--orange); border: 1px solid var(--yellow); color: var(--white); font-family: inherit; font-size: 9px; font-weight: 700; display: flex; align-items: center; justify-content: center; }
  .divider { left: 331px; top: 975px; height: 150px; border-left: 1px dashed #cfcfd8; }
  .info { left: 417px; display: flex; gap: 7px; align-items: flex-start; font-size: 9px; font-style: italic; color: var(--muted); line-height: 1.3; white-space: nowrap; }
  .info svg { flex: none; margin-top: 1px; }

  /* Footer */
  .footer { left: 0; top: 1145px; width: 667px; height: 55px; background: var(--footer-bg); }
  .legal { left: 108px; top: 1160px; font-family: "Arimo", Arial, sans-serif; font-size: 6.5px; color: var(--footer-text); line-height: 1.9; }
  .footer-social { left: 467px; top: 1163px; color: var(--white); }
</style>
</head>
<body>

<section class="hero abs" role="img" aria-label="Photo of a yellow-trailered truck driving at sunset in front of a city skyline"></section>
<div class="hero-photo abs" aria-hidden="true"></div>

<div class="brand abs"><i class="mark"></i>Dorrance Haul Co<small>Harlow Springs</small><small>555-014-2290</small></div>

<nav class="nav abs">
  <a class="active" href="#" style="left:0">HOME</a>
  <a href="#" style="left:50px">About</a>
  <a href="#" style="left:96px">News</a>
  <a href="#" style="left:140px">Services</a>
  <a href="#" style="left:195px">Contact</a>
</nav>
<div class="social hero-social abs" aria-label="Social links"><span></span><span></span><span></span><span></span></div>

<h1 class="hero-title abs">Lorem ipsum dolor</h1>
<p class="hero-text abs">nostrud exerci tation ullamcorper suscipit lobortis nisl ut aliquip ex ea commodo consequat. Duis autem vel eum iriure dolor in hendrerit in vulputate velit esse molestie consequat</p>
<a class="btn-outline abs"><span>Learn More</span></a>
<div class="dots abs"><i class="on"></i><i></i><i></i><i></i></div>

<h2 class="about-title abs">ABOUT</h2>
<p class="about-text abs">nostrud exerci tation ullamcorper suscipit lobortis nisl ut aliquip ex ea commodo consequat. Duis autem vel eum iriure dolor in hendrerit in vulputate velit esse molestie consequat.nostrud exerci tation ullamcorper suscipit lobortis nisl ut aliquip ex ea commodo consequat. Duis autem vel eum iriure dolor in hendrerit in vulputate velit esse molestie consequat</p>

<div class="split-left abs"></div>
<div class="split-right abs"></div>
<div class="dash abs" style="top:532px"></div>
<div class="dash abs" style="top:768px"></div>

<h2 class="split-heading who-title abs">WHO WE ARE</h2>
<p class="split-text who-text abs">nostrud exerci tation ullamcorper suscipit lobortis nisl ut aliquip ex ea commodo consequat. Duis autem vel eum iriure dolor in hendrerit in vulputate velit esse molestie consequat.nostrud exerci tation ullamcorper suscipit lobortis nisl ut aliquip ex ea commodo consequat. Duis autem vel eum iriure dolor in hendrerit in vulputate velit esse molestie consequat nostrud exerci tation ullamcorper suscipit lobortis nisl ut aliquip ex ea commodo consequat. Duis autem vel eum iriure dolor in hendrerit in vulputate velit esse molestie consequat.nostrud exerci tation ullamcorper suscipit lobortis nisl ut aliquip ex ea commodo consequat. Duis autem vel eum iriure dolor in hendrerit in vulputate velit esse molestie consequat</p>
<a class="learn-more who-more abs">Learn more</a>

<h2 class="split-heading what-title abs">WHAT WE DO</h2>
<p class="split-text what-text abs">nostrud exerci tation ullamcorper suscipit lobortis nisl ut aliquip ex ea commodo consequat. Duis autem vel eum iriure dolor in hendrerit in vulputate velit esse molestie consequat.nostrud exerci tation ullamcorper suscipit lobortis nisl ut aliquip ex ea commodo consequat. Duis autem vel eum iriure dolor in hendrerit in vulputate velit esse molestie consequat nostrud exerci tation ullamcorper suscipit lobortis nisl ut aliquip ex ea commodo consequat. Duis autem vel eum iriure dolor in hendrerit in vulputate velit esse molestie consequat.nostrud exerci tation ullamcorper suscipit lobortis nisl ut aliquip ex ea commodo consequat. Duis autem vel eum iriure dolor in hendrerit in vulputate velit esse molestie consequat</p>
<a class="learn-more what-more abs">Learn more</a>

<div class="split-brand abs"><i></i>Dorrance Haul Co</div>

<section class="band abs" role="img" aria-label="Photo of a red truck cab at dusk with construction cranes behind"></section>
<h2 class="band-title abs">MAKING<br>TRANSPORTATION<br>FAST AND SAFE</h2>
<p class="band-text abs">nostrud exerci tation ullamcorper suscipit lobortis nisl ut aliquip ex ea commodo consequat. Duis autem vel eum iriure dolor in hendrerit in vulputate velit esse molestie consequat.</p>
<a class="learn-more band-more abs">Learn more</a>

<section class="contact abs"></section>
<h2 class="contact-title abs">CONTACT US</h2>
<div class="field abs" style="top:1003px">NAME</div>
<div class="field abs" style="top:1029px">PHONE</div>
<div class="field abs" style="top:1058px">EMAIL</div>
<button class="submit abs">SUBMIT</button>
<div class="divider abs"></div>

<div class="info abs" style="top:1008px">
  <svg width="11" height="13" viewBox="0 0 11 13" fill="none" stroke="#d64d27" stroke-width="1.2"><path d="M5.5 12C5.5 12 1 7.5 1 5a4.5 4.5 0 0 1 9 0c0 2.5-4.5 7-4.5 7Z"/><circle cx="5.5" cy="5" r="1.6"/></svg>
  <span>4180 W. Prairie Line Rd ,<br>60999</span>
</div>
<div class="info abs" style="top:1046px">
  <svg width="11" height="11" viewBox="0 0 11 11" fill="none" stroke="#d64d27" stroke-width="1.2"><path d="M2 1h2l1 2.5-1.3 1a6 6 0 0 0 2.8 2.8l1-1.3L10 7v2a1 1 0 0 1-1 1A8 8 0 0 1 1 2a1 1 0 0 1 1-1Z"/></svg>
  <span>555,014,2290</span>
</div>
<div class="info abs" style="top:1069px">
  <svg width="12" height="11" viewBox="0 0 12 11" fill="#d64d27"><path d="M1 3.5C1 2 3 1 6 1s5 1 5 2.5V5H8.5V3.8h-5V5H1Z"/><rect x="2" y="6" width="8" height="4.5" rx="1"/></svg>
  <span>555,014,2291</span>
</div>
<div class="info abs" style="top:1093px">
  <svg width="11" height="9" viewBox="0 0 11 9" fill="none" stroke="#d64d27" stroke-width="1.1"><rect x=".6" y=".6" width="9.8" height="7.8"/><path d="M.6.6 5.5 5l4.9-4.4"/></svg>
  <span>dispatch@dorrancehaul.example</span>
</div>

<footer class="footer abs"></footer>
<p class="legal abs">COPYRIGHT © 2017 Dorrance Haul Co<br>TERMS &nbsp;| &nbsp;ALL RIGHTS RESERVED</p>
<div class="social footer-social abs" aria-label="Social links"><span></span><span></span><span></span><span></span></div>

</body>
</html>
```